Modern Design Business Card industrial maintenance company

Business card design for Company named Brookvale Equipment Services

Target Market(s)

Industrial

Industry/Entity Type

Maintenance and repair

Contact Information for Business Card

Place holder for address, office phone, mobile number and email

Requirements
Must have
• Clean modern look
Nice to have
• N/a

```html
<!DOCTYPE html>
<html lang="en">
<head>
<meta charset="utf-8">
<title>Brookvale Equipment Services – Business Card</title>
<link rel="stylesheet" href="https://fonts.googleapis.com/css2?family=Michroma&family=Poppins:wght@400&display=swap">
<style>
  :root {
    --backdrop: #bdbdbd;
    --card-light: #ffffff;
    --card-dark: #000000;
    --ink: #111111;
    --ink-soft: #2a2a2a;
    --paper-ink: #ffffff;
  }
  * { box-sizing: border-box; margin: 0; padding: 0; }
  html, body { width: 1093px; height: 1200px; overflow: hidden; }
  body {
    background: var(--backdrop);
    position: relative;
    font-family: "Poppins", sans-serif;
    color: var(--ink);
  }
  .card {
    position: absolute;
    left: 265px;
    border-radius: 26px;
    overflow: hidden;
  }
  .card--front { top: 226px; width: 577px; height: 344px; background: var(--card-light); }
  .card--back { top: 621px; width: 583px; height: 360px; background: var(--card-dark); }

  .holder-bar { position: absolute; left: 0; top: 43px; width: 18px; height: 35px; background: var(--ink); }
  .holder-name {
    position: absolute; left: 27px; top: 44px;
    font-family: "Michroma", sans-serif; font-size: 15.5px; font-weight: 400; letter-spacing: .3px; line-height: 1;
  }
  .holder-role { position: absolute; left: 26px; top: 60px; font-size: 17px; line-height: 1.2; color: var(--ink-soft); }

  .brand { position: absolute; text-align: center; font-family: "Michroma", sans-serif; }
  .brand__mark { display: block; margin: 0 auto; }
  .brand__name { display: block; line-height: 1; white-space: nowrap; }
  .brand__tag { display: block; line-height: 1; white-space: nowrap; }

  .card--front .brand { left: 302px; top: 30px; width: 280px; color: var(--ink); }
  .card--front .brand__name { margin-top: 10px; font-size: 20px; letter-spacing: 1.4px; padding-left: 1.4px; }
  .card--front .brand__tag { margin-top: 5px; font-size: 7.5px; letter-spacing: 5.4px; padding-left: 5.4px; }

  .card--back .brand { left: 71px; top: 86px; width: 441px; color: var(--paper-ink); }
  .card--back .brand__name { margin-top: 18px; font-size: 33px; letter-spacing: 2.4px; padding-left: 2.4px; }
  .card--back .brand__tag { margin-top: 9px; font-size: 11px; letter-spacing: 9px; padding-left: 9px; }

  .contact-list { position: absolute; left: 26px; top: 262px; list-style: none; }
  .contact-list li { display: flex; align-items: center; height: 21px; font-size: 17px; color: var(--ink-soft); }
  .contact-list svg { width: 19px; height: 19px; margin-right: 3px; flex: none; }

  .address { position: absolute; right: 25px; top: 283px; text-align: right; font-size: 17px; line-height: 21px; color: var(--ink-soft); font-style: normal; }
</style>
</head>
<body>
  <section class="card card--front">
    <div class="holder-bar"></div>
    <h1 class="holder-name">DANIEL HART</h1>
    <p class="holder-role">Managing Director</p>

    <div class="brand">
      <svg class="brand__mark" width="80" height="80" viewBox="0 0 80 80" aria-hidden="true">
        <circle cx="40" cy="40" r="37" fill="none" stroke="currentColor" stroke-width="4"/>
      </svg>
      <span class="brand__name">BROOKVALE</span>
      <span class="brand__tag">EQUIPMENT SERVICES</span>
    </div>

    <ul class="contact-list">
      <li>
        <svg viewBox="0 0 20 20" aria-hidden="true"><circle cx="10" cy="10" r="8.8" fill="none" stroke="#111" stroke-width="1.4"/><path d="M6.3 5.6l2 -.6 1.2 2.4-1.2 1c.6 1.4 1.5 2.3 2.9 2.9l1-1.2 2.4 1.2-.6 2c-3.9.2-7.7-3.6-7.7-7.7z" fill="#111"/></svg>
        044-870 312 564
      </li>
      <li>
        <svg viewBox="0 0 20 20" aria-hidden="true"><circle cx="10" cy="10" r="8.8" fill="none" stroke="#111" stroke-width="1.4"/><rect x="5.2" y="6.8" width="9.6" height="6.6" fill="#111"/><path d="M5.2 6.8l4.8 3.6 4.8-3.6" fill="none" stroke="#fff" stroke-width=".9"/></svg>
        hello@brookvale-es.com
      </li>
      <li>
        <svg viewBox="0 0 20 20" aria-hidden="true"><circle cx="10" cy="10" r="8.8" fill="none" stroke="#111" stroke-width="1.4"/><g fill="none" stroke="#111" stroke-width=".9"><circle cx="10" cy="10" r="4.6"/><ellipse cx="10" cy="10" rx="2" ry="4.6"/><path d="M5.4 10h9.2M6 7.8h8M6 12.2h8"/></g></svg>
        www.brookvale-es.com
      </li>
    </ul>

    <address class="address">18 Millbrook Road, Unit 4<br>40210, Eastfield</address>
  </section>

  <section class="card card--back">
    <div class="brand">
      <svg class="brand__mark" width="128" height="128" viewBox="0 0 128 128" aria-hidden="true">
        <circle cx="64" cy="64" r="61" fill="none" stroke="currentColor" stroke-width="4"/>
      </svg>
      <span class="brand__name">BROOKVALE</span>
      <span class="brand__tag">EQUIPMENT SERVICES</span>
    </div>
  </section>
</body>
</html>
```